Quarrystone Trading

The Business card will a 2 sided.
1) Front Side you will use logo1.png the other details will be
Martin Kelbrandtova
CTO
Quarry Stone Trading

+61 417 260 538
martin@quarrystonetrading.example
www.quarrystonetrading.example

2) Reverse side, needs to have all logo's 2,3,4,5,6,7 . png

the rest of the design is up to you

```html
<!DOCTYPE html>
<html lang="en">
<head>
<meta charset="utf-8">
<title>Quarrystone Trading — Business Card</title>
<link rel="stylesheet" href="https://fonts.googleapis.com/css2?family=Raleway:wght@400;500;700&display=swap">
<style>
  :root{
    --page:#ffffff;
    --card-top:#3b3b3d;
    --card-bottom:#1e1e1f;
    --accent:#1f73bf;
    --text-light:#f2f2f2;
    --text-muted:#cfcfcf;
    --mark:#c9c9cb;
    --divider:#8a8a8a;
  }
  *{box-sizing:border-box;margin:0;padding:0}
  html,body{width:1200px;height:900px;overflow:hidden;background:var(--page)}
  body{font-family:"Raleway",sans-serif;position:relative}
  .cards{position:absolute;left:20px;top:287px;display:flex;gap:20px}
  .card{
    position:relative;width:570px;height:326px;overflow:hidden;
    background:radial-gradient(ellipse at 55% 35%,var(--card-top) 0%,var(--card-bottom) 85%);
    box-shadow:0 6px 14px rgba(0,0,0,.35);
  }
  .card__band{position:absolute;left:0;right:0;bottom:0;height:11px;background:var(--accent)}

  .brand{display:flex;flex-direction:column;align-items:center;justify-content:center;gap:6px;color:var(--mark);font-weight:500;letter-spacing:.06em;text-transform:uppercase}
  .brand__row{display:flex;align-items:center;gap:8px;white-space:nowrap}
  .brand__dot{width:12px;height:12px;border-radius:50%;background:var(--mark);flex:none}
  .brand__region{font-size:9px;color:var(--text-muted);letter-spacing:.1em}

  .front .brand{position:absolute;left:0;right:0;top:40px;height:170px}
  .front .brand__name{font-size:22px}
  .front .brand__dot{width:16px;height:16px}

  .identity{position:absolute;right:288px;top:236px;text-align:right}
  .identity__name{color:var(--accent);font-weight:700;font-size:18px;white-space:nowrap}
  .identity__role{color:var(--text-light);font-size:12.5px;margin-top:3px}
  .identity__company{color:var(--text-light);font-size:15px;margin-top:8px;white-space:nowrap}
  .divider{position:absolute;left:292px;top:233px;width:1px;height:68px;background:var(--divider)}
  .contact{position:absolute;left:306px;top:238px;list-style:none;color:var(--text-light);font-size:12px}
  .contact li{display:flex;align-items:center;gap:8px;height:20px;white-space:nowrap}
  .contact svg{width:11px;height:11px;flex:none}
  .contact .hl{color:var(--accent)}

  .back .grid{position:absolute;left:30px;top:40px;width:510px;height:250px;display:grid;grid-template-columns:repeat(3,1fr);grid-template-rows:repeat(2,1fr)}
  .back .brand__name{font-size:10.5px;letter-spacing:.04em}
  .back .brand__dot{width:10px;height:10px}
  .back .brand__row{gap:6px}
</style>
</head>
<body>
<div class="cards">
  <section class="card front" aria-label="Card front">
    <div class="brand">
      <div class="brand__row"><span class="brand__dot"></span><span class="brand__name">Quarrystone Trading</span></div>
    </div>
    <div class="identity">
      <div class="identity__name">MARTIN KELBRANDTOVA</div>
      <div class="identity__role">CTO</div>
      <div class="identity__company">QUARRY STONE TRADING</div>
    </div>
    <div class="divider"></div>
    <ul class="contact">
      <li><svg viewBox="0 0 12 12" fill="none" stroke="#ddd" stroke-width="1"><circle cx="6" cy="6" r="5.3"/><path d="M4 3.5l1 1.2-.6.8c.5 1 1.1 1.6 2 2l.8-.6 1.2 1-.7.9c-2 0-3.8-1.8-4-4z" fill="#ddd"/></svg>+61 417 260 538</li>
      <li><svg viewBox="0 0 12 12" fill="none" stroke="#ddd" stroke-width="1"><circle cx="6" cy="6" r="5.3"/><rect x="3" y="4" width="6" height="4" fill="#ddd"/></svg>martin@quarrystonetrading.example</li>
      <li><svg viewBox="0 0 12 12" fill="none" stroke="#ddd" stroke-width="1"><circle cx="6" cy="6" r="5.3"/><circle cx="6" cy="6" r="3"/><path d="M3 6h6M6 3v6"/></svg><span>www.<span class="hl">quarrystonetrading</span>.example</span></li>
    </ul>
    <div class="card__band"></div>
  </section>

  <section class="card back" aria-label="Card back">
    <div class="grid">
      <div class="brand"><div class="brand__row"><span class="brand__dot"></span><span class="brand__name">Quarrystone Trading</span></div><span class="brand__region">Australia</span></div>
      <div class="brand"><div class="brand__row"><span class="brand__dot"></span><span class="brand__name">Quarrystone Trading</span></div><span class="brand__region">USA</span></div>
      <div class="brand"><div class="brand__row"><span class="brand__dot"></span><span class="brand__name">Quarrystone Trading</span></div><span class="brand__region">UK</span></div>
      <div class="brand"><div class="brand__row"><span class="brand__dot"></span><span class="brand__name">Quarrystone Trading</span></div><span class="brand__region">Asia</span></div>
      <div class="brand"><div class="brand__row"><span class="brand__dot"></span><span class="brand__name">Quarrystone Trading</span></div><span class="brand__region">China</span></div>
      <div class="brand"><div class="brand__row"><span class="brand__dot"></span><span class="brand__name">Quarrystone Trading</span></div><span class="brand__region">India</span></div>
    </div>
    <div class="card__band"></div>
  </section>
</div>
</body>
</html>
```